Mental Health

QRT HAVEN
Behavioral Health
4172 W. Pell St. Mesa, AZ 85219
Gwendolyn (480)555-0142 / Omar 480-555-0187

Email: QRTHaven@Mailvex.example
Newly Remodeled & Spacious
g Staff
Registered Nurses
Licensed Independent &
Professional Substance &
Abuse Counselors
Behavioral Health Techs
Certified Caregivers
Behavioral Health &
Substance Abuse Professionals

To Refer a Patient
About Us
QRT Haven is a Fully Staffed Behavioral
Health Residential Facility, providing
treatment plans for adults suffering
with various Behavioral Health and
Substance Abuse disorders, while living
in a nice safe, clean and supportive
environment. Our home offers clients the
ability to learn the necessary skills to
help clients adapt, build self confidence
as well as independence, with the goal
of reducing the probability of a future
crisis or possible relapse. We offer
counseling programs, consisting of a
variety of addiction and recovery support
groups, independent living, coping and
social skills groups, as well as assisting
clients with using tools to create a resume
to help obtain employment and so much
more. We are committed to teaching
self management care and allowing
clients to understand how to utilize the
resources, skills and tools available for
long term success by providing superior
quality, all-inclusive living arrangements
and treatment options.

Thank you for your patience while I update the final content needed for us to make the final decision this week.

```html
<!DOCTYPE html>
<html lang="en">
<head>
<meta charset="utf-8">
<title>QRT Haven Business Card</title>
<link rel="stylesheet" href="https://fonts.googleapis.com/css2?family=Merriweather:wght@300;400;700&family=Roboto:wght@300;400&display=swap">
<style>
  :root {
    --bg: #2b2b2b;
    --paper: #f3f3f1;
    --blue: #0f68b5;
    --blue-deep: #1a5fa8;
    --green: #6aaa3a;
    --teal: #2b8a8c;
    --orange: #e8782f;
    --yellow: #f2d43a;
    --ink: #333333;
    --muted: #6c6c6c;
    --faint: rgba(0,0,0,0.05);
  }
  * { box-sizing: border-box; margin: 0; padding: 0; }
  html, body { width: 1200px; height: 1200px; overflow: hidden; background: var(--bg); }
  .canvas { position: relative; width: 1200px; height: 1200px; }

  .card {
    position: absolute;
    width: 593px; height: 348px;
    background: var(--paper);
    border-radius: 24px;
    overflow: hidden;
  }
  .card--front { left: 298px; top: 200px; }
  .card--back { left: 292px; top: 637px; }

  .backdrop-circle {
    position: absolute;
    border-radius: 50%;
    border: 22px solid var(--faint);
  }
  .card--front .backdrop-circle { width: 380px; height: 380px; left: 240px; top: -10px; }
  .card--back .backdrop-circle { width: 380px; height: 380px; left: 320px; top: -10px; }

  .brand {
    position: absolute;
    display: flex; align-items: center; gap: 12px;
    font-family: "Merriweather", serif;
    font-weight: 400;
    color: var(--blue);
    letter-spacing: 2px;
    white-space: nowrap;
  }
  .brand__dot { width: 50px; height: 50px; border-radius: 50%; background: var(--green); flex: none; }
  .card--front .brand { left: 0; right: 0; top: 66px; justify-content: center; font-size: 40px; }
  .card--back .brand { left: 31px; top: 58px; font-size: 40px; }

  .services {
    position: absolute; left: 0; top: 177px;
    width: 100%; height: 123px;
    background: linear-gradient(90deg, var(--green) 0%, var(--teal) 60%, var(--blue-deep) 100%);
    display: flex; flex-direction: column; justify-content: center; align-items: center;
    font-family: "Merriweather", serif; font-weight: 300;
    font-size: 15px; line-height: 24.5px; color: #ffffff;
  }
  .services .sep { color: var(--yellow); margin: 0 8px; }

  .site-line {
    position: absolute; left: 0; right: 0; top: 311px;
    text-align: center;
    font-family: "Roboto", sans-serif; font-weight: 300;
    font-size: 15px; letter-spacing: 6px; color: var(--muted);
  }
  .site-line .b { color: var(--blue); }
  .site-line .o { color: var(--orange); }

  .person { position: absolute; left: 27px; top: 188px; }
  .person__name { font-family: "Merriweather", serif; font-weight: 700; font-size: 23px; color: var(--blue); }
  .person__role { font-family: "Roboto", sans-serif; font-weight: 300; font-size: 16px; color: var(--ink); margin-top: 2px; }

  .address {
    position: absolute; left: 25px; top: 267px;
    font-family: "Roboto", sans-serif; font-weight: 300;
    font-size: 16px; line-height: 24px; color: var(--ink);
  }

  .contacts {
    position: absolute; left: 320px; top: 187px;
    list-style: none;
    font-family: "Roboto", sans-serif; font-weight: 300;
    font-size: 16px; line-height: 24.5px; color: var(--ink);
  }
  .contacts li { display: flex; align-items: center; gap: 16px; }
  .contacts svg { width: 13px; height: 13px; flex: none; }

  .footer-strip {
    position: absolute; left: 0; bottom: 0; width: 280px; height: 12px; background: var(--green);
  }
  .footer-band {
    position: absolute; right: 0; bottom: 0; width: 340px; height: 42px;
    background: var(--blue);
    clip-path: polygon(22px 0, 100% 0, 100% 100%, 0 100%);
    display: flex; align-items: center; justify-content: flex-end; padding-right: 24px;
    font-family: "Roboto", sans-serif; font-weight: 300; font-size: 15.5px; color: #ffffff;
    letter-spacing: 0.2px;
  }
</style>
</head>
<body>
<main class="canvas">

  <section class="card card--front">
    <div class="backdrop-circle"></div>
    <div class="brand"><span class="brand__dot"></span><span>QRT HAVEN</span></div>
    <div class="services">
      <p>Newly Remodeled<span class="sep">|</span>Spacious Staff<span class="sep">|</span>Registered Nurses</p>
      <p>Licensed Independent<span class="sep">|</span>Professional Substance<span class="sep">|</span>Abuse Counselors</p>
      <p>Behavioral Health Techs<span class="sep">|</span>Certified Caregivers</p>
      <p>Behavioral Health<span class="sep">|</span>Substance Abuse Professionals</p>
    </div>
    <p class="site-line">www.<span class="b">qrthaven</span><span class="o">az</span>.example</p>
  </section>

  <section class="card card--back">
    <div class="backdrop-circle"></div>
    <div class="brand"><span class="brand__dot"></span><span>QRT HAVEN</span></div>

    <div class="person">
      <p class="person__name">Gwendolyn</p>
      <p class="person__role">Managing Director</p>
    </div>

    <p class="address">4172 W. Pell St.<br>Mesa, AZ 85219</p>

    <ul class="contacts">
      <li>
        <svg viewBox="0 0 16 16" aria-hidden="true"><path fill="#2b8a6a" d="M2 6c0-2 2-3 6-3s6 1 6 3v1h-3V6H5v1H2zM4 8h8l2 6H2z"/></svg>
        (480) 555-0142
      </li>
      <li>
        <svg viewBox="0 0 16 16" aria-hidden="true"><rect x="1" y="3" width="14" height="10" fill="#2b8a6a"/><path d="M1 3l7 6 7-6" fill="none" stroke="#fff" stroke-width="1.4"/></svg>
        QRTHaven@Mailvex.example
      </li>
      <li>
        <svg viewBox="0 0 16 16" aria-hidden="true"><circle cx="8" cy="8" r="6.5" fill="#2b8a6a"/><path d="M1.5 8h13M8 1.5c-3 3-3 10 0 13M8 1.5c3 3 3 10 0 13" fill="none" stroke="#fff" stroke-width="1"/></svg>
        www.qrthavenaz.example
      </li>
    </ul>

    <div class="footer-strip"></div>
    <div class="footer-band">QRT HAVEN | BEHAVIORAL HEALTH</div>
  </section>

</main>
</body>
</html>
```